Bourbon whiskey bottle label

I need a bottle label for bourbon whiskey. Size 3" x 5" max. I want design in the label and not a rectangle/square label.

tandrolux = bourbon whiskey = tandro lux

I've attached an example of a label that I really like so maybe this will help inspire.

I'm open to any colors. I want it to stand out. I do like the thought of a white layered background with color design.

I would like it to at least have the following on it:
-tandrolux (logo attached) or just add it yourself
-Private Barrel Select
-Straight Bourbon Whiskey
-Proof (plus little box to write)
-ALC/VOL (plus little box to write)
-Plus an open area (no design) to write message.

bourbon whiskey drinkers and industry

whiskey bourbon, retail

• see project description
• see project description
• see project description

```html
<!DOCTYPE html>
<html lang="en">
<head>
<meta charset="utf-8">
<title>Tandrolux – Private Barrel Select Label</title>
<link href="https://fonts.googleapis.com/css2?family=Permanent+Marker&family=Great+Vibes&family=Allura&display=swap" rel="stylesheet">
<style>
  :root {
    --canvas-bg: #ffffff;
    --label-navy: #10103e;
    --label-edge: #0a0a2c;
    --frame-blue: #8fd3f4;
    --ornament-blue: #9fd8f2;
    --script-cream: #f4eda4;
    --script-gold: #d9c47a;
    --ink-white: #ffffff;
    --rule-silver: #c9cde0;
  }
  html, body {
    margin: 0;
    padding: 0;
    width: 800px;
    height: 1200px;
    overflow: hidden;
    background: var(--canvas-bg);
  }
  .canvas {
    position: relative;
    width: 800px;
    height: 1200px;
  }
  .label {
    position: absolute;
    left: 55px;
    top: 95px;
    width: 690px;
    height: 1009px;
  }
  .label-body { fill: var(--label-navy); stroke: var(--label-edge); stroke-width: 6; }
  .label-frame { fill: none; stroke: var(--frame-blue); stroke-width: 4; }
  .crown-rule { fill: none; stroke: var(--rule-silver); stroke-width: 2; stroke-linecap: round; }
  .brand-name {
    font-family: "Permanent Marker", cursive;
    font-size: 66px;
    fill: var(--ink-white);
    letter-spacing: 1px;
  }
  .range-name {
    font-family: "Great Vibes", cursive;
    font-size: 56px;
    fill: var(--script-cream);
  }
  .spirit-type {
    font-family: "Allura", cursive;
    font-size: 44px;
    fill: var(--ink-white);
  }
  .field-label {
    font-family: "Allura", cursive;
    font-size: 32px;
    fill: var(--script-gold);
  }
  .write-box { fill: var(--ink-white); }
  .ornament-area { opacity: 0.5; }
</style>
</head>
<body>
<div class="canvas">
  <svg class="label" viewBox="480 1045 660 965" xmlns="http://www.w3.org/2000/svg">
    <defs>
      <linearGradient id="ornamentBlue" x1="0" y1="0" x2="1" y2="1">
        <stop offset="0" stop-color="#9fd8f2" stop-opacity="0.55"/>
        <stop offset="1" stop-color="#9fd8f2" stop-opacity="0.15"/>
      </linearGradient>
      <linearGradient id="ornamentGold" x1="0" y1="0" x2="1" y2="0">
        <stop offset="0" stop-color="#b9bcc8" stop-opacity="0.35"/>
        <stop offset="1" stop-color="#e6d38a" stop-opacity="0.35"/>
      </linearGradient>
    </defs>

    <path class="label-body" d="M 485 1160 L 600 1150 Q 700 1050 810 1050 Q 920 1050 1020 1150 L 1135 1160 L 1135 1175 L 1115 1190 L 1115 1480 L 1090 1500 A 60 60 0 0 0 1090 1620 L 1115 1640 L 1115 1855 L 1135 1870 L 1135 1885 L 1010 1890 Q 920 1995 810 1995 Q 700 1995 610 1890 L 485 1885 L 485 1870 L 505 1855 L 505 1640 L 530 1620 A 60 60 0 0 0 530 1500 L 505 1480 L 505 1190 L 485 1175 Z"/>
    <path class="label-frame" transform="translate(810 1522) scale(0.965 0.972) translate(-810 -1522)" d="M 485 1160 L 600 1150 Q 700 1050 810 1050 Q 920 1050 1020 1150 L 1135 1160 L 1135 1175 L 1115 1190 L 1115 1480 L 1090 1500 A 60 60 0 0 0 1090 1620 L 1115 1640 L 1115 1855 L 1135 1870 L 1135 1885 L 1010 1890 Q 920 1995 810 1995 Q 700 1995 610 1890 L 485 1885 L 485 1870 L 505 1855 L 505 1640 L 530 1620 A 60 60 0 0 0 530 1500 L 505 1480 L 505 1190 L 485 1175 Z"/>

    <g class="crown-rules">
      <path class="crown-rule" d="M 720 1108 Q 810 1096 900 1108"/>
      <path class="crown-rule" d="M 660 1128 Q 810 1112 960 1128"/>
      <path class="crown-rule" d="M 630 1152 Q 810 1134 990 1154"/>
    </g>

    <rect class="ornament-area" role="img" aria-label="Blue filigree corner scroll" x="522" y="1172" width="90" height="100" rx="30" fill="url(#ornamentBlue)"/>
    <rect class="ornament-area" role="img" aria-label="Blue filigree corner scroll" x="1005" y="1172" width="90" height="100" rx="30" fill="url(#ornamentBlue)"/>
    <rect class="ornament-area" role="img" aria-label="Blue filigree corner scroll" x="522" y="1775" width="90" height="105" rx="30" fill="url(#ornamentBlue)"/>
    <rect class="ornament-area" role="img" aria-label="Blue filigree corner scroll" x="1005" y="1775" width="90" height="105" rx="30" fill="url(#ornamentBlue)"/>

    <text class="brand-name" x="810" y="1262" text-anchor="middle">TANDROLUX</text>
    <text class="range-name" x="810" y="1358" text-anchor="middle">Private Barrel Select</text>

    <rect class="ornament-area" role="img" aria-label="Silver and gold flourish divider" x="555" y="1372" width="530" height="105" rx="50" fill="url(#ornamentGold)"/>

    <text class="spirit-type" x="810" y="1745" text-anchor="middle">Straight Bourbon Whiskey</text>

    <rect class="ornament-area" role="img" aria-label="Gold flourish divider" x="560" y="1762" width="500" height="52" rx="26" fill="url(#ornamentGold)"/>

    <text class="field-label" x="752" y="1866" text-anchor="end">Proof</text>
    <rect class="write-box" x="790" y="1835" width="93" height="40"/>
    <text class="field-label" x="770" y="1934" text-anchor="end">Alc/Vol</text>
    <rect class="write-box" x="790" y="1903" width="93" height="40"/>
  </svg>
</div>
</body>
</html>
```